Stationary

We have designed a new logo and business care.
It is now time for stationary.
We are a financial planning firm and are looking for something more formal that show the strength of our firm.
Please include our tag line; Integrity - Vision -Diligence.
I have uploaded a PDF of our current stationary - but - you are under no obligation to design anything like it.
Thx
Marta

```html
<!DOCTYPE html>
<html lang="en">
<head>
<meta charset="utf-8">
<title>Harbor Summit Group — Stationery</title>
<link href="https://fonts.googleapis.com/css2?family=Questrial&family=Montserrat:wght@400;600&display=swap" rel="stylesheet">
<style>
  :root{
    --navy:#353a85;
    --blue:#2c77bd;
    --paper:#f6f6f7;
    --ink:#3a3a44;
    --backdrop:#d2d2d4;
  }
  *{box-sizing:border-box;margin:0;padding:0}
  html,body{width:1200px;height:1000px;overflow:hidden;background:var(--backdrop)}
  .canvas{position:relative;width:1200px;height:1000px;font-family:'Questrial',sans-serif;color:var(--ink)}
  .sheet{position:absolute;background:var(--paper);overflow:hidden}
  .brand{position:absolute;left:0;right:0;text-align:center}
  .brand-name{font-family:'Questrial',sans-serif;color:var(--navy);white-space:nowrap;line-height:1}
  .brand-tag{font-family:'Montserrat',sans-serif;color:var(--ink);white-space:nowrap;line-height:1}
  .brand.on-dark .brand-name,.brand.on-dark .brand-tag{color:#fff}
  .top-arc{position:absolute;left:0;top:0;width:100%;height:6px}
  .contact{position:absolute;left:0;right:0;text-align:center;font-family:'Montserrat',sans-serif;color:var(--ink);line-height:1.45}
  .contact-icons{display:block;margin:0 auto}

  /* folder */
  .folder{left:152px;top:42px;width:430px;height:558px;background:#f7f7f8}
  .folder-wave{position:absolute;inset:0}
  .folder .brand{top:110px}
  .folder .brand-name{font-size:22px}
  .folder .brand-tag{font-size:8px;letter-spacing:3.6px;margin-top:9px}
  .folder-web{position:absolute;left:0;right:0;top:518px;text-align:center;color:#fff;font-family:'Montserrat',sans-serif;font-size:8.5px}
  .folder-web strong{font-weight:600}

  /* letterhead */
  .letterhead{left:616px;top:61px;width:417px;height:539px}
  .letterhead .brand{top:68px}
  .letterhead .brand-name{font-size:14px}
  .letterhead .brand-tag{font-size:5.5px;letter-spacing:2.6px;margin-top:6px}
  .letter-body{position:absolute;left:38px;top:164px;width:340px;font-family:'Montserrat',sans-serif;font-size:5.6px;line-height:7.6px;text-align:justify;color:#444}
  .letter-body p{margin-bottom:9px}
  .letter-body .salutation{font-weight:600;margin-bottom:12px}
  .sign-off{position:absolute;left:38px;top:340px;font-family:'Montserrat',sans-serif;font-size:5.6px;line-height:1.4;color:#444}
  .sign-off strong{font-weight:600}
  .signature{position:absolute;left:90px;top:330px;width:90px;height:34px;background:linear-gradient(90deg,#e9ecf6,#dfe4f3);border-radius:3px}
  .letterhead .contact{top:494px;font-size:5.6px}
  .letterhead .contact-icons{width:92px;height:12px;margin-bottom:5px}

  /* envelope front */
  .envelope-front{left:117px;top:629px;width:466px;height:203px}
  .envelope-front .brand{top:42px}
  .envelope-front .brand-name{font-size:13.5px}
  .envelope-front .brand-tag{font-size:5.3px;letter-spacing:2.5px;margin-top:5px}
  .envelope-front .contact{top:155px;font-size:5.4px}
  .envelope-front .contact-icons{width:92px;height:12px;margin-bottom:5px}

  /* envelope back */
  .envelope-back{left:616px;top:629px;width:466px;height:203px}
  .envelope-flap{position:absolute;left:0;top:0;width:466px;height:68px}
  .envelope-back .brand{top:30px}
  .envelope-back .brand-name{font-size:10px}

  /* business cards */
  .card-back{left:410px;top:861px;width:172px;height:99px;background:var(--navy)}
  .card-back .brand{top:38px}
  .card-back .brand-name{font-size:8.5px}
  .card-back .brand-tag{font-size:3.6px;letter-spacing:1.6px;margin-top:4px}
  .card-front{left:616px;top:861px;width:173px;height:99px}
  .card-front .brand{top:20px}
  .card-front .brand-name{font-size:7.5px}
  .card-front .brand-tag{font-size:3.2px;letter-spacing:1.5px;margin-top:3px}
  .card-person{position:absolute;left:0;right:0;top:52px;text-align:center;font-family:'Montserrat',sans-serif}
  .card-person .person-name{font-size:5px;font-weight:600;color:var(--navy);letter-spacing:.3px;text-transform:uppercase}
  .card-person .person-role{font-size:3.8px;margin-top:2px}
  .card-front .contact{top:69px;font-size:3.7px}
  .card-front .contact-icons{width:46px;height:6px;margin-bottom:3px}
</style>
</head>
<body>
<svg width="0" height="0" style="position:absolute" aria-hidden="true">
  <defs>
    <symbol id="contact-row" viewBox="0 0 120 16">
      <line x1="0" y1="8" x2="120" y2="8" stroke="#2c77bd" stroke-width="1"/>
      <g fill="#fff" stroke="#2c77bd" stroke-width="1.2">
        <circle cx="33" cy="8" r="6.5"/><circle cx="51" cy="8" r="6.5"/>
        <circle cx="69" cy="8" r="6.5"/><circle cx="87" cy="8" r="6.5"/>
      </g>
      <path d="M29.5 8.2 L33 5 L36.5 8.2 M30.8 7.4 V11 H35.2 V7.4" fill="none" stroke="#2c77bd" stroke-width="1"/>
      <path d="M48.6 5.2 Q48 8.5 51.5 11 L53 9.8 L51.8 8.6 L51 9.2 Q49.8 8.2 49.8 6.8 L50.6 6.2 L49.6 5 Z" fill="#2c77bd"/>
      <rect x="66.3" y="7" width="5.4" height="3" fill="none" stroke="#2c77bd" stroke-width="0.9"/>
      <rect x="67.5" y="4.8" width="3" height="2.2" fill="#2c77bd"/>
      <circle cx="87" cy="8" r="3.2" fill="none" stroke="#2c77bd" stroke-width="0.9"/>
      <path d="M83.8 8 H90.2 M87 4.8 V11.2" stroke="#2c77bd" stroke-width="0.7"/>
    </symbol>
  </defs>
</svg>

<main class="canvas">

  <section class="sheet folder">
    <svg class="folder-wave" viewBox="0 0 430 558" preserveAspectRatio="none" aria-hidden="true">
      <path d="M0 194 C120 226 300 226 430 170 L430 558 L0 558 Z" fill="var(--blue)"/>
      <path d="M0 199 C130 233 300 229 430 190 L430 558 L0 558 Z" fill="var(--navy)"/>
      <rect x="27" y="0" width="2" height="558" fill="#000" opacity="0.08"/>
    </svg>
    <div class="brand">
      <div class="brand-name">Harbor Summit Group</div>
      <div class="brand-tag">Clarity Balance Endurance</div>
    </div>
    <div class="folder-web">www.<strong>HarborSummitGroup</strong>.com</div>
  </section>

  <section class="sheet letterhead">
    <svg class="top-arc" viewBox="0 0 417 6" preserveAspectRatio="none" aria-hidden="true">
      <path d="M45 0 H372 Q208 6 45 0 Z" fill="var(--navy)"/>
    </svg>
    <div class="brand">
      <div class="brand-name">Harbor Summit Group</div>
      <div class="brand-tag">Clarity Balance Endurance</div>
    </div>
    <div class="letter-body">
      <p class="salutation">Dear sir,</p>
      <p>Thank you for the trust you have placed in our team. Our planners review each portfolio with care, weigh every option against your long term goals, and explain each step in plain words so that you always know where your money stands and why.</p>
      <p>This year we have added quarterly reviews, clearer statements and a direct line to your advisor. These changes came from your feedback, and we will keep listening as markets shift and your plans grow. Our aim is simple: steady guidance you can rely on for decades.</p>
      <p>Please review the enclosed summary before our next meeting. If anything looks unclear, call our office and a member of the team will gladly walk you through it.</p>
      <p>We look forward to working with you in the years ahead.</p>
    </div>
    <div class="sign-off">Yours Sincerely,<br><strong>Dana Whitford</strong></div>
    <div class="signature" role="img" aria-label="Handwritten signature of Dana Whitford"></div>
    <div class="contact">
      <svg class="contact-icons" aria-hidden="true"><use href="#contact-row"/></svg>
      2250 W. Larchmont Ave., Fairview, WA 99001<br>
      (555) 014-2210 &nbsp;|&nbsp; (555) 014-2211 &nbsp;|&nbsp; www.HarborSummitGroup.com
    </div>
  </section>

  <section class="sheet envelope-front">
    <svg class="top-arc" viewBox="0 0 466 6" preserveAspectRatio="none" aria-hidden="true">
      <path d="M65 0 H400 Q232 6 65 0 Z" fill="var(--navy)"/>
    </svg>
    <div class="brand">
      <div class="brand-name">Harbor Summit Group</div>
      <div class="brand-tag">Clarity Balance Endurance</div>
    </div>
    <div class="contact">
      <svg class="contact-icons" aria-hidden="true"><use href="#contact-row"/></svg>
      2250 W. Larchmont Ave., Fairview, WA 99001<br>
      (555) 014-2210 &nbsp;|&nbsp; (555) 014-2211 &nbsp;|&nbsp; www.HarborSummitGroup.com
    </div>
  </section>

  <section class="sheet envelope-back">
    <svg class="envelope-flap" viewBox="0 0 466 68" aria-hidden="true">
      <path d="M0 0 H466 L450 60 Q448 66 440 66 H26 Q18 66 16 60 Z" fill="var(--navy)"/>
    </svg>
    <div class="brand on-dark">
      <div class="brand-name">Harbor Summit Group</div>
    </div>
  </section>

  <section class="sheet card-back">
    <div class="brand on-dark">
      <div class="brand-name">Harbor Summit Group</div>
      <div class="brand-tag">Clarity Balance Endurance</div>
    </div>
  </section>

  <section class="sheet card-front">
    <svg class="top-arc" viewBox="0 0 173 4" preserveAspectRatio="none" aria-hidden="true" style="height:4px">
      <path d="M25 0 H148 Q86 4 25 0 Z" fill="var(--navy)"/>
    </svg>
    <div class="brand">
      <div class="brand-name">Harbor Summit Group</div>
      <div class="brand-tag">Clarity Balance Endurance</div>
    </div>
    <div class="card-person">
      <div class="person-name">Owen Lisle</div>
      <div class="person-role">General Manager</div>
    </div>
    <div class="contact">
      <svg class="contact-icons" aria-hidden="true"><use href="#contact-row"/></svg>
      2250 W. Larchmont Ave., Fairview, WA 99001<br>
      (555) 014-2210 | (555) 014-2211 | www.HarborSummitGroup.com
    </div>
  </section>

</main>
</body>
</html>
```